Brindle Supports

We need an updated website that captures the comprehensive services and supports we provide to persons with developmental disabilities. We need a website design that educates families about the services we provide. We would also need a website that is user-friendly so that we could periodically update training schedules and ongoing programming.

• Thank you for submitting designs.  A few things I am hoping to see offered in the website:
• Front page highlights the services we offer (host homes, family caregiver, day program, employment program, SLS program, supported apartment program, behavior/clinical program)
• Front page also highlights any new programs we want to make prominent:  family caregiver, future restaurant employment openings, etc...
• Interactive Training Calendar
• Employee Resources page (link to carvix, email login, etc.)
• Uniform provider application for host home providers
• Information on agency - history, goals, etc.
• Contact Information/Location

 

Fun things to include:

• Client Highlights (featuring a client story each month, etc...)
• Employee highlights (featuring a staff member...)
• link to other Brindle business pages (Brindle Therapy and Brindle Restaurant)

```html
<!DOCTYPE html>
<html lang="en">
<head>
<meta charset="utf-8">
<title>Brindle Supports</title>
<link href="https://fonts.googleapis.com/css2?family=Alegreya:wght@400;700&family=Fondamento&family=Didact+Gothic&family=Cutive&display=swap" rel="stylesheet">
<style>
:root{
  --maroon:#7a2a28;
  --maroon-dark:#5e1f1d;
  --ink:#1c1c1c;
  --grey-text:#5a5a5a;
  --page:#f4f4f3;
  --rule:#d9d9d6;
  --white:#ffffff;
}
*{margin:0;padding:0;box-sizing:border-box}
html,body{width:1116px;height:1200px;overflow:hidden}
body{background:var(--page);position:relative;font-family:"Alegreya",serif;color:var(--ink)}
.abs{position:absolute}

.site-header{left:0;top:0;width:1116px;height:93px;background:#fafafa;border-bottom:2px solid var(--maroon)}
.nav a{position:absolute;top:41px;font-family:"Alegreya",serif;font-weight:700;font-size:16px;color:var(--ink);text-decoration:none}
.nav a.active{color:var(--maroon)}
.brand{left:462px;top:26px;width:230px;display:flex;align-items:center;gap:8px}
.brand-dot{width:22px;height:22px;border-radius:50%;background:var(--maroon);flex:none}
.brand-name{font-family:"Alegreya",serif;font-weight:700;font-size:22px;color:var(--maroon);white-space:nowrap}

.hero{left:0;top:93px;width:1116px;height:355px;background:linear-gradient(90deg,#e6eaf0 0%,#d8d2cc 30%,#e9e6e3 55%,#cfd5de 80%,#eef1f5 100%)}

.service-photo{width:148px;height:148px;border-radius:50%;border:4px solid var(--white);box-shadow:0 1px 4px rgba(0,0,0,.25)}
.photo-desk{left:206px;top:407px;background:radial-gradient(circle at 45% 55%,#e8922c,#9a4a1a)}
.photo-training{left:470px;top:407px;background:radial-gradient(circle at 50% 50%,#f2f2f2,#b9bdc3)}
.photo-support{left:768px;top:407px;background:radial-gradient(circle at 60% 50%,#d9c2a8,#4a4a4a)}

.service{width:250px;text-align:center;top:564px}
.service h3{font-weight:700;font-size:19px;color:var(--maroon);margin-bottom:9px}
.service p{font-size:13.5px;line-height:18.6px;color:var(--ink)}
.vrule{width:1px;background:var(--rule)}
.hrule{height:1px;background:var(--rule)}

.welcome-title{left:116px;top:708px;font-family:"Fondamento",cursive;font-size:28px;color:var(--ink)}
.welcome-title span{color:var(--maroon)}
.welcome-copy{left:116px;top:752px;width:302px;font-size:13.5px;line-height:18.6px;text-align:justify}
.welcome-copy p+p{margin-top:18.6px}
.welcome-photo{left:435px;top:760px;width:246px;height:162px;border:3px solid var(--white);box-shadow:0 0 3px rgba(0,0,0,.2);background:linear-gradient(120deg,#cfd6de,#f1ece6 45%,#9aa5b5)}
.btn-more{left:116px;top:931px;width:98px;height:27px;border-radius:5px;background:linear-gradient(#8d3733,var(--maroon-dark));color:#f0dcda;font-family:"Cutive",serif;font-size:14px;line-height:27px;text-align:center;text-decoration:none}

.updates-title{left:743px;top:708px;font-family:"Fondamento",cursive;font-size:28px;color:var(--maroon)}
.update{left:743px;width:240px}
.update-head{display:flex;align-items:center;gap:8px}
.date{width:35px;height:29px;border:1px solid #cfcfcf;background:var(--white);text-align:center;font-family:Arial,sans-serif}
.date b{display:block;height:9px;background:var(--maroon);color:#f3d9d7;font-size:7px;line-height:9px;font-weight:400}
.date i{font-style:normal;font-size:15px;line-height:18px;color:var(--grey-text)}
.update h4{font-family:"Fondamento",cursive;font-weight:400;font-size:20px;color:var(--maroon)}
.update p{margin-top:7px;font-family:Arial,sans-serif;font-size:11.3px;line-height:13.4px;color:var(--grey-text)}

.tweets-title{left:186px;top:1038px;font-family:"Didact Gothic",sans-serif;font-size:30px;color:#444}
.tweet-dots{left:384px;top:1020px}
.tweet-mark{left:414px;top:1030px;width:90px;height:90px;border-radius:50%;background:#e2e2e0}
.tweet-text{left:529px;top:1040px;width:420px;font-family:Arial,sans-serif;font-size:13px;line-height:16px;color:#444}

.site-footer{left:0;top:1147px;width:1116px;height:53px;background:var(--maroon);font-family:Arial,sans-serif;font-size:13.5px;color:var(--white)}
.site-footer a{position:absolute;top:18px;color:var(--white);text-decoration:none}
.copyright{position:absolute;left:652px;top:18px}
</style>
</head>
<body>

<header class="abs site-header">
  <nav class="nav">
    <a class="active" href="#" style="left:126px">Home</a>
    <a href="#" style="left:205px">About Us</a>
    <a href="#" style="left:302px">Our Service</a>
    <a href="#" style="left:728px">Our News</a>
    <a href="#" style="left:828px">Contact Us</a>
    <a href="#" style="left:932px">Faq</a>
  </nav>
  <div class="abs brand"><span class="brand-dot"></span><span class="brand-name">Brindle Supports</span></div>
</header>

<div class="abs hero" role="img" aria-label="Team of business people working together at a conference table with laptops"></div>

<div class="abs service-photo photo-desk" role="img" aria-label="Wooden meeting table with a laptop"></div>
<div class="abs service-photo photo-training" role="img" aria-label="Presenter at a flip chart with staff"></div>
<div class="abs service-photo photo-support" role="img" aria-label="Support agent with a headset"></div>

<section class="abs service" style="left:155px">
  <h3>Host Home Services</h3>
  <p>Lorem ipsum dolor sit amet, con-<br>sectetur adipiscing elit. Curabitur<br>dapibus suscipit tempor.</p>
</section>
<div class="abs vrule" style="left:412px;top:465px;height:186px"></div>
<section class="abs service" style="left:421px">
  <h3>Employee Services</h3>
  <p>Lorem ipsum dolor sit amet, con-<br>sectetur adipiscing elit. Curabitur<br>dapibus suscipit tempor.</p>
</section>
<div class="abs vrule" style="left:710px;top:465px;height:186px"></div>
<section class="abs service" style="left:719px">
  <h3>Client Supports</h3>
  <p>Lorem ipsum dolor sit amet, con-<br>sectetur adipiscing elit. Curabitur<br>dapibus suscipit tempor.</p>
</section>

<div class="abs hrule" style="left:110px;top:688px;width:871px"></div>

<h2 class="abs welcome-title">Welcome to <span>Brindle Supports</span></h2>
<div class="abs welcome-copy">
  <p>Lorem ipsum dolor sit amet, consectetur adipiscing elit. Curabitur dapibus suscipit tempor. Lorem ipsum dolor sit amet, consectetur adipiscing elit. Curabitur dapibus suscipit tempor.</p>
  <p>Lorem ipsum dolor sit amet, consectetur adipiscing elit. Curabitur dapibus suscipit tempor. Lorem ipsum dolor sit amet, Lorem ipsum dolor sit amet, consectetur adipiscing elit. Curabitur dapibus.</p>
</div>
<div class="abs welcome-photo" role="img" aria-label="Smiling woman at an office desk with colleagues behind"></div>
<a class="abs btn-more" href="#">Read More</a>

<div class="abs vrule" style="left:710px;top:707px;height:260px"></div>

<h2 class="abs updates-title">Our Updates....</h2>
<article class="abs update" style="top:758px">
  <div class="update-head"><div class="date"><b>JAN</b><i>31</i></div><h4>Lorem ipsum dolor</h4></div>
  <p>Lorem ipsum dolor sit amet, consectetur adipiscing elit. Curabitur dapibus suscipit tempor. Proin ut libero felis. Integer placerat ultricies nunc at dignissim.</p>
</article>
<article class="abs update" style="top:869px">
  <div class="update-head"><div class="date"><b>JAN</b><i>27</i></div><h4>Lorem ipsum dolor</h4></div>
  <p>Lorem ipsum dolor sit amet, consectetur adipiscing elit. Curabitur dapibus suscipit tempor. Proin ut libero felis. Integer placerat ultricies nunc at dignissim.</p>
</article>

<div class="abs hrule" style="left:110px;top:993px;width:871px"></div>

<h2 class="abs tweets-title" style="font-weight:400">Latest Tweets</h2>
<svg class="abs tweet-dots" width="14" height="80" viewBox="0 0 14 80" aria-hidden="true">
  <g fill="#f4f4f3" stroke="#d4d4d2"><circle cx="7" cy="6" r="5"/><circle cx="7" cy="26" r="5"/><circle cx="7" cy="46" r="5"/><circle cx="7" cy="66" r="5"/></g>
</svg>
<div class="abs tweet-mark"></div>
<p class="abs tweet-text">Lorem ipsum dolor sit amet, consectetur adipiscing elit. Ut odio lacus, commodo sit amet euismod accumsan, condimentum vel mi ! ! !</p>

<footer class="abs site-footer">
  <a href="#" style="left:133px">Home</a>
  <a href="#" style="left:204px">Menu</a>
  <a href="#" style="left:273px">Events</a>
  <a href="#" style="left:349px">Contact Us</a>
  <span class="copyright">Copyright © 2014 Brindle Support - All rights reserved</span>
</footer>

</body>
</html>
```